I already have a business sign that has what I want on my business cards, however it needs to be modified to make a double sided business card. Also the wording needs modification. I want the Harbourlight Tennis Coaching logo on the front of the business card with the Black/Green background. And I want the tennis ball dot points on the back of the card with the green background. The dot points as follows:
-All Ages Welcome
-Qualified, Enthusiastic Coaches
-Group, Semi Private & Private Lessons
-Beginner, Intermediate and Advanced Standards
-Pulse Rally
-Mini Aces

Also, I want the "A GREAT WAY TO GET FIT AND HEALTHY" to remain as is, and my name and number.
I've added a file that has my current signage, as a guide.

```html
<!DOCTYPE html>
<html lang="en">
<head>
<meta charset="utf-8">
<title>Harbourlight Tennis Coaching – Business Card Back</title>
<link rel="stylesheet" href="https://fonts.googleapis.com/css2?family=Barlow:wght@500&family=Oswald:wght@600&family=Arimo&display=swap">
<style>
  :root {
    --ink: #000000;
    --court-green: #9dff00;
    --ball-green: #b4f214;
    --ball-light: #d9ff6a;
    --paper: #ffffff;
  }
  * { margin: 0; padding: 0; box-sizing: border-box; }
  html, body {
    width: 1200px;
    height: 900px;
    overflow: hidden;
    background: var(--paper);
  }
  .canvas {
    position: relative;
    width: 1200px;
    height: 900px;
  }
  .side-label {
    position: absolute;
    top: 62px;
    left: 0;
    width: 1200px;
    text-align: center;
    font-family: "Arimo", Arial, sans-serif;
    font-size: 96px;
    line-height: 1;
    color: var(--ink);
  }
  .card {
    position: absolute;
    left: 75px;
    top: 218px;
    width: 1050px;
    height: 600px;
  }
  .card-art {
    position: absolute;
    inset: 0;
  }
  .bullet-rail {
    position: absolute;
    left: 53px;
    top: 117px;
    width: 45px;
    height: 325px;
    background: var(--ink);
    border-radius: 12px;
  }
  .bullet-rail .dot {
    position: absolute;
    left: 13px;
    width: 19px;
    height: 19px;
    border-radius: 50%;
    background: radial-gradient(circle at 40% 35%, var(--ball-light), var(--court-green) 60%, #6fb800);
  }
  .features {
    position: absolute;
    left: 113px;
    top: 122px;
    list-style: none;
    font-family: "Barlow", "DIN Alternate", sans-serif;
    font-weight: 500;
    font-size: 39px;
    line-height: 53.6px;
    color: var(--ink);
    text-shadow: 1.5px 1.5px 0 rgba(255,255,255,0.85);
    white-space: nowrap;
  }
  .contact {
    position: absolute;
    left: 0;
    top: 490px;
    width: 1050px;
    height: 98px;
    font-family: "Oswald", "Bebas Neue", sans-serif;
    font-weight: 600;
    color: var(--paper);
    text-transform: uppercase;
  }
  .contact-name {
    position: absolute;
    right: 580px;
    top: 20px;
    font-size: 48px;
    line-height: 1;
    letter-spacing: 0.5px;
  }
  .contact-divider {
    position: absolute;
    left: 503px;
    top: 0;
    width: 4px;
    height: 98px;
    background: var(--paper);
  }
  .contact-phone {
    position: absolute;
    left: 535px;
    top: 14px;
    font-size: 56px;
    line-height: 1;
    letter-spacing: 1px;
  }
</style>
</head>
<body>
<main class="canvas">
  <h1 class="side-label">Back</h1>

  <section class="card" aria-label="Harbourlight Tennis Coaching business card, back">
    <svg class="card-art" width="1050" height="600" viewBox="0 0 1050 600" aria-hidden="true">
      <rect class="card-field" x="0" y="0" width="1050" height="600" fill="var(--court-green)"/>
      <rect class="top-band" x="0" y="0" width="1050" height="32" fill="var(--ink)"/>
      <path class="ball-notch" d="M843 20 H1020 V136 Q1020 164 992 164 H871 Q843 164 843 136 Z" fill="var(--ink)"/>
      <path class="contact-band" d="M24 590 V527 Q24 477 74 477 H976 Q1026 477 1026 527 V590 Z" fill="var(--ink)"/>
      <rect class="bottom-edge" x="0" y="590" width="1050" height="10" fill="var(--ink)"/>
      <circle class="tennis-ball" cx="926" cy="85" r="57" fill="var(--ball-green)" role="img" aria-label="Tennis ball illustration"/>
    </svg>

    <div class="bullet-rail" aria-hidden="true">
      <span class="dot" style="top:18px"></span>
      <span class="dot" style="top:72px"></span>
      <span class="dot" style="top:126px"></span>
      <span class="dot" style="top:179px"></span>
      <span class="dot" style="top:233px"></span>
      <span class="dot" style="top:287px"></span>
    </div>

    <ul class="features">
      <li>All Ages Welcome</li>
      <li>Qualified, Enthusiastic Coaches</li>
      <li>Group, Semi Private &amp; Private Lessons</li>
      <li>Beginner, Intermediate and Advanced Standards</li>
      <li>Pulse Rally</li>
      <li>Mini Aces</li>
    </ul>

    <div class="contact">
      <span class="contact-name">Sam Delaney</span>
      <span class="contact-divider" aria-hidden="true"></span>
      <span class="contact-phone">0400 555 318</span>
    </div>
  </section>
</main>
</body>
</html>
```